Velmint website

A clean uncluttered design that shows at glance that we are in the Media and design and publishing business.

We would like to see designs that use colours that show warmth and quality.

The website should show:
- products
- projects

These should be displaxed in spaces that we can add or interchanges with new products or projects.
Updates

Target Market(s)

Business and project managers and buyers and authors.

Industry/Entity Type

Business

Requirements
Must have
• Good colours. Not too strong, not weak, but reflecting quality.

```html
<!DOCTYPE html>
<html lang="en">
<head>
<meta charset="utf-8">
<title>Velmint — Media, Design &amp; Publishing</title>
<link href="https://fonts.googleapis.com/css2?family=Roboto:wght@300;400;500;700&family=Oswald:wght@600&display=swap" rel="stylesheet">
<style>
  :root {
    --ink: #222222;
    --bronze: #9b7556;
    --bronze-dark: #86623f;
    --header-bg: #ffffff;
    --hero-bg: #ededed;
    --sand: #f1e7d6;
    --footer-bg: rgba(222, 201, 162, 0.9);
    --navy: #26324f;
    --thumb-shadow: rgba(0,0,0,0.25);
  }
  * { box-sizing: border-box; margin: 0; padding: 0; }
  html, body { width: 1200px; height: 1029px; overflow: hidden; }
  body { font-family: "Roboto", Arial, sans-serif; color: var(--ink); background: var(--hero-bg); }
  .page { position: relative; width: 1200px; height: 1029px; overflow: hidden; }

  .hero-band { position: absolute; left: 0; top: 100px; width: 1200px; height: 522px; background: var(--hero-bg); }
  .sand-band { position: absolute; left: 0; top: 622px; width: 1200px; height: 274px; background: var(--sand); }

  .feature-photo { position: absolute; left: 712px; top: 112px; width: 268px; height: 917px; z-index: 0;
    border-radius: 120px 120px 40px 40px;
    background: linear-gradient(180deg,
      rgba(38,50,79,0.85) 0%, rgba(38,50,79,0.9) 10%,
      rgba(214,190,170,0.75) 14%, rgba(214,190,170,0.7) 20%,
      rgba(38,50,79,0.92) 26%, rgba(38,50,79,0.92) 54%,
      rgba(230,228,224,0.8) 60%,
      rgba(186,120,100,0.7) 68%, rgba(120,130,170,0.7) 78%,
      rgba(200,170,90,0.65) 88%, rgba(150,150,110,0.5) 100%); }

  .site-header { position: absolute; left: 0; top: 0; width: 1200px; height: 100px; background: var(--header-bg);
    box-shadow: 0 10px 16px -8px rgba(0,0,0,0.22); z-index: 3; }
  .brand { position: absolute; left: 172px; top: 20px; font-weight: 300; font-size: 70px; letter-spacing: 1px; color: var(--ink); line-height: 1; }
  .main-nav a { position: absolute; top: 68px; font-size: 12.5px; color: var(--bronze); text-decoration: none; letter-spacing: 0.3px; }
  .main-nav a.is-active { font-weight: 700; color: var(--bronze-dark); border-bottom: 3px solid var(--bronze); padding: 0 18px 0 0; }
  .phone { position: absolute; left: 895px; top: 62px; font-size: 19px; color: var(--bronze); }
  .util-btn { position: absolute; top: 23px; width: 29px; height: 27px; background: var(--bronze); }

  .headline { position: absolute; left: 174px; top: 228px; z-index: 2; }
  .headline .we { font-family: "Oswald", sans-serif; font-weight: 600; font-size: 54px; color: var(--bronze); line-height: 1; letter-spacing: -1px; }
  .headline .are { font-family: "Oswald", sans-serif; font-weight: 600; font-size: 29px; color: var(--ink); }
  .headline .line { display: block; font-weight: 300; font-size: 42.5px; line-height: 62px; letter-spacing: -0.5px; }

  .showcase { position: absolute; left: 173px; top: 523px; width: 856px; height: 123px; z-index: 2; }
  .showcase-item { position: absolute; top: 0; width: 201px; height: 123px; box-shadow: 0 1px 4px var(--thumb-shadow); overflow: hidden; }
  .showcase-item .art { position: absolute; inset: 0; }
  .item-1 { left: 0; background: #fff; }
  .item-1 .art { background: radial-gradient(ellipse at 50% 50%, #3a8fb8 0%, #6bbf6a 30%, #d9e6ee 55%, #ffffff 75%); }
  .item-2 { left: 220px; top: -3px; box-shadow: 0 2px 8px rgba(0,0,0,0.5); }
  .item-2 .art { background: linear-gradient(90deg, #7a2a08 0%, #e2791c 35%, #f0a02a 55%, #8a3f18 100%); }
  .item-2 .caption { position: absolute; left: 0; bottom: 0; width: 100%; height: 31px; background: rgba(20,20,20,0.8);
    color: #fff; font-weight: 700; font-size: 11px; padding: 9px 12px; }
  .item-2 svg { position: absolute; right: 12px; bottom: 6px; }
  .item-3 { left: 440px; }
  .item-3 .art { background: radial-gradient(ellipse at 55% 60%, #e8e8e8 0%, #b5b5b5 30%, #3a3530 60%, #1a1715 100%); }
  .item-4 { left: 654px; background: #fff; }
  .item-4 .art { background: radial-gradient(ellipse at 50% 55%, #d8c850 0%, #d04a9a 20%, #3a9ad8 35%, #ececec 55%, #ffffff 75%); }

  .intro { position: absolute; left: 174px; top: 696px; font-weight: 300; font-size: 27px; line-height: 31px;
    text-transform: uppercase; letter-spacing: -0.4px; z-index: 2; }

  .site-footer { position: absolute; left: 0; top: 896px; width: 1200px; height: 133px; background: var(--footer-bg); z-index: 1; }
  .social { position: absolute; left: 189px; top: 939px; display: flex; gap: 6px; z-index: 2; }
  .social span { width: 50px; height: 50px; border-radius: 50%; background: #b0a89a; border: 3px solid #efe9df; box-shadow: 0 1px 3px rgba(0,0,0,0.3); }
  .social span.is-first { background: #2f4f9a; }
  .footer-brand { position: absolute; right: 180px; top: 915px; font-weight: 300; font-size: 66px; color: var(--ink); line-height: 1; z-index: 2; }
  .copyright { position: absolute; right: 180px; top: 991px; font-size: 9.5px; color: var(--ink); z-index: 2; }
</style>
</head>
<body>
<div class="page">
  <div class="hero-band"></div>
  <div class="sand-band"></div>

  <div class="feature-photo" role="img" aria-label="Photo of a man in a navy uniform and cap with brightly patterned flower trousers"></div>

  <header class="site-header">
    <div class="brand">Velmint</div>
    <nav class="main-nav">
      <a class="is-active" href="#" style="left:440px">HOME</a>
      <a href="#" style="left:545px">PRODUCTS</a>
      <a href="#" style="left:669px">PROJECTS</a>
      <a href="#" style="left:782px">CONTACT</a>
    </nav>
    <div class="phone">(855) 41 62 70 8</div>
    <a class="util-btn" href="#" style="left:966px" aria-label="Log in">
      <svg width="29" height="27" viewBox="0 0 29 27"><path d="M17 8h3v11h-3M9 13.5h8M13.5 10l3.5 3.5-3.5 3.5" fill="none" stroke="#fff" stroke-width="1.8"/></svg>
    </a>
    <a class="util-btn" href="#" style="left:999px" aria-label="Search">
      <svg width="29" height="27" viewBox="0 0 29 27"><circle cx="12.5" cy="11.5" r="4" fill="none" stroke="#fff" stroke-width="2"/><path d="M15.5 14.5l5 5" stroke="#fff" stroke-width="2.4"/></svg>
    </a>
  </header>

  <h1 class="headline">
    <span class="we">WE</span><span class="are">ARE</span>
    <span class="line">IN THE MEDIA AND DESIGN</span>
    <span class="line">AND PUBLISHING</span>
    <span class="line">BUSINESS.</span>
  </h1>

  <section class="showcase">
    <div class="showcase-item item-1"><div class="art" role="img" aria-label="Fan of printed brochures and magazines"></div></div>
    <div class="showcase-item item-2">
      <div class="art" role="img" aria-label="Orange printed cards project on a wooden table"></div>
      <div class="caption">See Project</div>
      <svg width="22" height="22" viewBox="0 0 22 22"><circle cx="9" cy="9" r="6.5" fill="none" stroke="#fff" stroke-width="1.8"/><path d="M9 6v6M6 9h6M14 14l6 6" stroke="#fff" stroke-width="1.8"/></svg>
    </div>
    <div class="showcase-item item-3"><div class="art" role="img" aria-label="White business card on a dark surface"></div></div>
    <div class="showcase-item item-4"><div class="art" role="img" aria-label="Row of colour ink cartridges"></div></div>
  </section>

  <p class="intro">Lorem ipsum dolor sit amet,<br>consectetuer adipiscing elit, sed<br>diam nonummy nibh euismod<br>tincidunt ut laoreet dolore magna<br>aliquam erat volutpat.</p>

  <footer class="site-footer"></footer>
  <div class="social" aria-label="Social links"><span class="is-first"></span><span></span><span></span></div>
  <div class="footer-brand">Velmint</div>
  <div class="copyright">COPYRIGHT © 2014 Velmint Media Design &amp; Publishing. ALL RIGHTS RESERVED.</div>
</div>
</body>
</html>
```